Needing a business Card for new fire company.

Velm, sales fire equipment and parts. We also do tree clearing for the forest service. My logo will be attached to this. I am also looking for a design that when people see the card it stick with them and they will remember my sales team giving it to them.

```html
<!DOCTYPE html>
<html lang="en">
<head>
<meta charset="utf-8">
<title>Velm Business Card</title>
<link href="https://fonts.googleapis.com/css2?family=Montserrat:wght@400;500;700&display=swap" rel="stylesheet">
<style>
  :root {
    --page: #ecebe8;
    --ink: #0b0b0b;
    --ink-soft: #1c1c1c;
    --paper: #ffffff;
    --paper-shade: #eeeeee;
    --flame: #c4262e;
    --text-dark: #141414;
    --text-light: #f4f4f4;
  }
  * { margin: 0; padding: 0; box-sizing: border-box; }
  html, body { width: 1200px; height: 914px; overflow: hidden; background: var(--page); }
  body { position: relative; font-family: "Montserrat", sans-serif; }

  .card {
    position: absolute;
    left: 230px;
    width: 740px;
    height: 423px;
    overflow: hidden;
    box-shadow: 0 6px 18px rgba(0,0,0,.25);
  }
  .card-front { top: 22px; background: radial-gradient(ellipse at 50% 45%, var(--ink-soft), var(--ink) 75%); }
  .card-back { top: 469px; background: var(--ink); }

  .wordmark {
    position: absolute;
    color: var(--text-light);
    font-weight: 700;
    letter-spacing: 0.06em;
    line-height: 1;
    display: flex;
    align-items: center;
  }
  .wordmark .mark-square {
    display: inline-block;
    background: var(--flame);
    margin-right: 0.3em;
  }
  .card-front .wordmark { left: 0; right: 0; top: 160px; justify-content: center; font-size: 104px; }
  .card-front .mark-square { width: 44px; height: 44px; }
  .card-back .wordmark { left: 64px; top: 48px; font-size: 52px; }
  .card-back .mark-square { width: 22px; height: 22px; }

  .back-shape { position: absolute; inset: 0; width: 100%; height: 100%; }

  .contact-list { position: absolute; left: 44px; top: 262px; list-style: none; }
  .contact-list li {
    display: flex; align-items: center; gap: 12px;
    font-size: 16px; color: var(--text-dark); margin-bottom: 7px;
  }
  .contact-list svg { width: 16px; height: 16px; fill: var(--flame); flex: none; }

  .holder { position: absolute; right: 40px; top: 168px; text-align: right; }
  .holder-name { color: var(--flame); font-weight: 700; font-size: 30px; letter-spacing: 0.02em; }
  .holder-role { color: var(--text-light); font-size: 17px; letter-spacing: 0.04em; margin-top: 4px; }

  .address { position: absolute; right: 44px; bottom: 22px; text-align: right; color: var(--text-dark); }
  .address-company { display: flex; justify-content: flex-end; align-items: center; gap: 8px; font-weight: 700; font-size: 18px; letter-spacing: 0.05em; margin-bottom: 4px; color: var(--text-dark); }
  .address-company svg { width: 14px; height: 18px; fill: var(--flame); }
  .address-line { font-size: 16px; line-height: 1.35; }
</style>
</head>
<body>
  <section class="card card-front">
    <div class="wordmark"><span class="mark-square"></span>VELM</div>
  </section>

  <section class="card card-back">
    <svg class="back-shape" viewBox="0 0 740 423" preserveAspectRatio="none" aria-hidden="true">
      <defs>
        <linearGradient id="paperFade" x1="0" y1="0" x2="0" y2="1">
          <stop offset="0" stop-color="#eeeeee"/>
          <stop offset="1" stop-color="#ffffff"/>
        </linearGradient>
      </defs>
      <path d="M0,118 C220,215 470,275 740,282 L740,423 L0,423 Z" fill="#ffffff"/>
      <path d="M0,128 C220,222 470,280 740,285 L740,423 L0,423 Z" fill="var(--flame)"/>
      <path d="M0,150 C220,240 470,290 740,290 L740,423 L0,423 Z" fill="url(#paperFade)"/>
    </svg>

    <div class="wordmark"><span class="mark-square"></span>VELM</div>

    <ul class="contact-list">
      <li><svg viewBox="0 0 24 24"><path d="M6.6 10.8a15.1 15.1 0 0 0 6.6 6.6l2.2-2.2c.3-.3.7-.4 1-.2 1.1.4 2.3.6 3.6.6.6 0 1 .4 1 1V20c0 .6-.4 1-1 1C10.6 21 3 13.4 3 4c0-.6.4-1 1-1h3.5c.6 0 1 .4 1 1 0 1.3.2 2.5.6 3.6.1.3 0 .7-.2 1z"/></svg>(555) 214-3090</li>
      <li><svg viewBox="0 0 24 24"><path d="M2 5h20v14H2zM3.5 6.5 12 13l8.5-6.5z" fill-rule="evenodd"/></svg>info@velm.com</li>
      <li><svg viewBox="0 0 24 24"><path d="M12 2a10 10 0 1 0 0 20 10 10 0 0 0 0-20zm0 2c.9 1.1 1.7 2.8 2 5h-4c.3-2.2 1.1-3.9 2-5zM4.3 11h3.8c0-.7.1-1.4.2-2H5a8 8 0 0 0-.7 2zm0 2A8 8 0 0 0 5 15h3.3c-.1-.6-.2-1.3-.2-2zm5.8 0c0 .7.1 1.4.2 2h3.4c.1-.6.2-1.3.2-2zm0-2h3.8c0-.7-.1-1.4-.2-2h-3.4c-.1.6-.2 1.3-.2 2zm5.8 0h3.8a8 8 0 0 0-.7-2h-3.3c.1.6.2 1.3.2 2zm0 2c0 .7-.1 1.4-.2 2H19a8 8 0 0 0 .7-2zM12 20c-.9-1.1-1.7-2.8-2-5h4c-.3 2.2-1.1 3.9-2 5z"/></svg>www.velm.com</li>
    </ul>

    <div class="holder">
      <p class="holder-name">Daniel Hart</p>
      <p class="holder-role">General Manager</p>
    </div>

    <div class="address">
      <p class="address-company"><svg viewBox="0 0 14 18"><path d="M7 0a7 7 0 0 0-7 7c0 5 7 11 7 11s7-6 7-11a7 7 0 0 0-7-7zm0 9.5A2.5 2.5 0 1 1 7 4.5a2.5 2.5 0 0 1 0 5z"/></svg>VELM</p>
      <p class="address-line">Your Address Here</p>
      <p class="address-line">2nd Line adress</p>
    </div>
  </section>
</body>
</html>
```